Retractable Banner Design for Youth Group

I would like the signage with the following as well as the following:
YOUTH VISION: Realigning the blueprint of our youth to God’s original plan.
YOUTH MISSION: Developing a generation of young people who are confident of God's irrefutable love; healing power; mercy and forgiveness; and, sovereignty.

The banner size is 33.5x 79 inches

Target Market(s)

Teenagers

Industry/Entity Type

Religious

Colors

Designer to choose colors to be used in the design.

Requirements
Must have
• Logo
• Inner Healing
• Discipleship
• Leadership Development

```html
<!DOCTYPE html>
<html lang="en">
<head>
<meta charset="utf-8">
<title>Rising Youth – Retractable Banner</title>
<link href="https://fonts.googleapis.com/css2?family=Montserrat:wght@400;500;600;700;800&display=swap" rel="stylesheet">
<style>
  :root {
    --brand-red: #9b1620;
    --deep-red: #8a121b;
    --ink: #3d3d3f;
    --paper: #ffffff;
    --stage: #e4e4e6;
    --soft-white: #e9dfe0;
    --icon-grey: #4a4a4c;
    --icon-disc: #e8e8e8;
  }
  * { box-sizing: border-box; margin: 0; padding: 0; }
  html, body {
    width: 1200px; height: 1200px; overflow: hidden;
    background: var(--stage);
    font-family: "Montserrat", sans-serif;
  }
  .banner {
    position: absolute; left: 361px; top: 40px;
    width: 478px; height: 1120px;
    background: var(--paper);
    box-shadow: 0 6px 24px rgba(0,0,0,.12);
    overflow: hidden;
  }
  .banner-shapes { position: absolute; inset: 0; }
  .brand {
    position: absolute; left: 0; right: 0; top: 38px;
    display: flex; flex-direction: column; align-items: center; gap: 22px;
  }
  .brand-dot {
    width: 84px; height: 84px; border-radius: 50%;
    background: var(--brand-red);
  }
  .brand-name {
    color: var(--brand-red);
    font-weight: 600; font-size: 30px; letter-spacing: 2px;
    text-transform: uppercase;
  }
  .statement {
    position: absolute; left: 0; right: 0;
    display: flex; flex-direction: column; align-items: center;
    text-align: center; color: var(--soft-white);
  }
  .statement--vision { top: 644px; }
  .statement--mission { top: 745px; }
  .pill {
    background: var(--paper); color: var(--brand-red);
    font-weight: 800; font-size: 23px; line-height: 1;
    padding: 5px 12px 4px; border-radius: 9px;
    margin-bottom: 9px; letter-spacing: .2px;
  }
  .statement p { font-size: 17.5px; line-height: 23px; font-weight: 500; }
  .statement--mission p { font-size: 17px; line-height: 21.5px; }
  .statement strong { color: var(--paper); font-weight: 700; }
  .pillars {
    position: absolute; left: 0; right: 0; top: 900px;
    display: flex; justify-content: center; gap: 32px;
  }
  .pillar { width: 100px; display: flex; flex-direction: column; align-items: center; }
  .pillar-badge {
    width: 98px; height: 98px; border-radius: 50%;
    border: 1.5px dashed rgba(255,255,255,.85);
    display: flex; align-items: center; justify-content: center;
  }
  .pillar-badge svg { width: 84px; height: 84px; }
  .pillar-label {
    margin-top: 8px; color: var(--paper);
    font-weight: 700; font-size: 13.5px; line-height: 15px; text-align: center;
  }
  .site-url {
    position: absolute; left: 0; right: 0; top: 1064px;
    text-align: center; font-weight: 800; font-size: 24px; color: var(--ink);
    letter-spacing: -.2px;
  }
  .site-url span { color: var(--brand-red); }
</style>
</head>
<body>
<main class="banner">
  <svg class="banner-shapes" viewBox="0 0 478 1120" width="478" height="1120" aria-hidden="false">
    <defs>
      <linearGradient id="field-tone" x1="0" y1="0" x2="0" y2="1">
        <stop offset="0" stop-color="#d4d4d4"/>
        <stop offset=".45" stop-color="#a9a9a9"/>
        <stop offset="1" stop-color="#4f4f4f"/>
      </linearGradient>
    </defs>
    <!-- red body -->
    <rect x="0" y="520" width="478" height="532" fill="var(--brand-red)"/>
    <!-- photo area -->
    <path role="img" aria-label="Black and white photo of four young women seen from behind in a wheat field, raising their hands in heart shapes"
          d="M0 270 C 50 290 120 292 220 256 S 400 196 478 210 L 478 560 C 400 540 300 570 200 610 C 120 640 50 640 0 636 Z"
          fill="url(#field-tone)"/>
    <!-- top red ribbon -->
    <path d="M0 262 C 50 284 120 286 220 250 S 400 190 478 202 L 478 210 C 400 196 320 222 220 256 C 120 292 50 290 0 270 Z"
          fill="var(--brand-red)"/>
    <!-- white ribbon above red body -->
    <path d="M0 636 C 50 640 120 640 200 610 C 300 570 400 540 478 560 L 478 574 C 400 556 300 586 200 626 C 120 656 50 656 0 652 Z"
          fill="var(--paper)"/>
    <path d="M0 652 C 50 656 120 656 200 626 C 300 586 400 556 478 574 L 478 600 L 0 680 Z" fill="var(--brand-red)"/>
    <!-- footer -->
    <rect x="0" y="1052" width="478" height="68" fill="var(--paper)"/>
  </svg>

  <header class="brand">
    <div class="brand-dot"></div>
    <div class="brand-name">Rising Youth</div>
  </header>

  <section class="statement statement--vision">
    <h2 class="pill">YOUTH VISION</h2>
    <p><strong>Realigning</strong> the blueprint of our youth to<br><strong>God’s original plan.</strong></p>
  </section>

  <section class="statement statement--mission">
    <h2 class="pill">YOUTH MISSION</h2>
    <p>Developing a generation of young people<br>who are confident of <strong>God's irrefutable<br>love; healing power; mercy and<br>forgiveness; and, sovereignty.</strong></p>
  </section>

  <ul class="pillars">
    <li class="pillar">
      <div class="pillar-badge">
        <svg viewBox="0 0 84 84">
          <circle cx="42" cy="42" r="40" fill="var(--icon-disc)"/>
          <circle cx="42" cy="44" r="14" fill="var(--icon-grey)"/>
          <g stroke="var(--icon-grey)" stroke-width="3" stroke-linecap="round">
            <line x1="42" y1="16" x2="42" y2="23"/><line x1="22" y1="25" x2="27" y2="30"/>
            <line x1="62" y1="25" x2="57" y2="30"/><line x1="15" y1="44" x2="21" y2="44"/>
            <line x1="69" y1="44" x2="63" y2="44"/>
          </g>
          <path d="M20 60 Q42 70 64 56" stroke="var(--icon-grey)" stroke-width="5" fill="none" stroke-linecap="round"/>
        </svg>
      </div>
      <span class="pillar-label">Inner Healing</span>
    </li>
    <li class="pillar">
      <div class="pillar-badge">
        <svg viewBox="0 0 84 84">
          <circle cx="42" cy="42" r="40" fill="var(--icon-disc)"/>
          <path d="M16 26 Q30 22 41 28 V60 Q30 54 16 58 Z" fill="var(--icon-grey)"/>
          <path d="M68 26 Q54 22 43 28 V60 Q54 54 68 58 Z" fill="var(--icon-grey)"/>
          <path d="M12 30 V62 Q28 58 42 64 Q56 58 72 62 V30" stroke="var(--icon-grey)" stroke-width="3" fill="none"/>
        </svg>
      </div>
      <span class="pillar-label">Discipleship</span>
    </li>
    <li class="pillar">
      <div class="pillar-badge">
        <svg viewBox="0 0 84 84">
          <circle cx="42" cy="42" r="40" fill="var(--icon-disc)"/>
          <g fill="var(--icon-grey)">
            <circle cx="42" cy="22" r="5"/><rect x="37" y="29" width="10" height="26" rx="3"/>
            <rect x="34" y="56" width="16" height="6" rx="1"/>
            <circle cx="20" cy="38" r="3.5"/><rect x="16.5" y="43" width="7" height="14" rx="2"/>
            <circle cx="28" cy="38" r="3.5"/><rect x="24.5" y="43" width="7" height="14" rx="2"/>
            <circle cx="56" cy="38" r="3.5"/><rect x="52.5" y="43" width="7" height="14" rx="2"/>
            <circle cx="64" cy="38" r="3.5"/><rect x="60.5" y="43" width="7" height="14" rx="2"/>
          </g>
        </svg>
      </div>
      <span class="pillar-label">Leadership Development</span>
    </li>
  </ul>

  <footer class="site-url">www.<span>risingyouthgroup</span>.org</footer>
</main>
</body>
</html>
```